Medical Practice Brochure Design Project

We are a medical practice in Denver, Colorado and we need to design a brochure to promote one subset of services we offer. We perform Bureau of Freight Haulage (BFH) physical exams and also perform BFH drug testing onsite and want a brochure that outlines these services. This brochure will be used a part of a marketing package to promote this service to businesses that employ individuals that drive commercial vehicles.

Project Deadline Extended Reason: I am going extend the deadline for submissions. Ending on a Sunday is going to limit last minute submissions. As a trade off, I am going to guarantee this project. Thanks for all the submissions. Added Thursday, October 09, 2014

Target Market(s)

human resource managers, companies that deploy commercial vehicles (i.e. trucks and tractor trailers), independent drivers / contractors

Industry/Entity Type

Medical

Font styles to use
Sans Serif

Colors
0455a3

Requirements
Must have
• Our logo, our web address (kellanmoorclinic.com), our phone number and fax number, professional look and feel, layout be a trifold 8.5x11 (see templates), map to our location (see attached for example).
Nice to have
• Our logo (birchwell family medicine) should not be the focus of the brochure. Text items that should stand out should be "BFH Examination", "BFH Drug Testing" and "QWLPA Certified Providers", our phone number, and our web address. We also will have the ability to have clients schedule appointment online through our website which should be indicated in the brochure in a prominent manner.
Should not have
• no images of crosses, no images of syringes

```html
<!DOCTYPE html>
<html lang="en">
<head>
<meta charset="utf-8">
<title>Birchwell Family Medicine – BFH Exams Brochure</title>
<link href="https://fonts.googleapis.com/css2?family=Open+Sans:ital,wght@0,400;0,600;0,700;1,400&family=PT+Sans+Narrow:wght@700&display=swap" rel="stylesheet">
<style>
  :root{
    --brand-blue:#0455a3;
    --deep-blue:#0a3f8f;
    --light-blue:#3f7fd0;
    --accent-red:#e3141b;
    --ink:#4a4a4a;
    --paper:#ffffff;
    --stage:#e9edf2;
  }
  *{box-sizing:border-box;margin:0;padding:0}
  html,body{width:1200px;height:1093px;overflow:hidden;background:var(--stage)}
  body{font-family:"Open Sans",Arial,sans-serif;position:relative}
  .sheet{position:absolute;left:0;top:82px;width:1200px;height:929px;background:var(--paper);overflow:hidden}
  .photo{position:absolute}
  .photo--staff{left:0;top:0;width:413px;height:480px;
    background:linear-gradient(160deg,#eef3f8 0%,#dfe7ef 45%,#f4e6e4 80%,#ffffff 100%)}
  .photo--driver{left:780px;top:190px;width:420px;height:290px;
    background:linear-gradient(120deg,#ffffff 0%,#cfe1f3 35%,#7fb0e0 60%,#e8dcc6 85%,#ffffff 100%)}
  .fold{position:absolute;top:0;width:14px;height:470px;background:linear-gradient(90deg,rgba(0,0,0,.06),rgba(0,0,0,0))}
  .fold--one{left:413px}.fold--two{left:815px}
  .waves{position:absolute;left:0;top:0;width:1200px;height:929px}
  .brand{position:absolute;color:var(--brand-blue);font-weight:600;text-transform:uppercase;line-height:1.05}
  .brand--small{left:62px;top:66px;font-size:15px;letter-spacing:.5px}
  .brand--large{left:845px;top:50px;font-size:30px;letter-spacing:.5px}
  .panel-center{position:absolute;left:413px;top:0;width:402px;text-align:center;color:var(--ink)}
  .cta-top{margin-top:55px;font-size:23px;line-height:33px;color:var(--brand-blue)}
  .cta-top .cta-lead{color:var(--accent-red);font-weight:700;display:block}
  .visit-title{margin-top:42px;font-family:"PT Sans Narrow",Arial,sans-serif;font-weight:700;font-size:33px;color:#555}
  .address{margin-top:18px;font-size:18px;line-height:29px;text-transform:uppercase}
  .contact{margin-top:22px;font-size:18px;line-height:29px;text-transform:uppercase}
  .contact span{display:inline-block;width:270px;text-align:left}
  .map{position:absolute;left:436px;top:490px;width:316px;height:264px;background:linear-gradient(180deg,#e8eef7,#dce6f2);border:1px solid #c9d6e8}
  .directions{position:absolute;left:425px;top:772px;width:380px;text-align:center;color:#fff;font-style:italic;font-size:14.5px;line-height:20.5px;text-transform:uppercase}
  .about{position:absolute;left:30px;top:560px;width:337px;text-align:right;color:#fff;font-size:18.5px;line-height:25px}
  .about h2{font-weight:400;font-size:28px;line-height:34px}
  .about p+p{margin-top:22px}
  .services{position:absolute;left:820px;top:540px;width:341px;text-align:right;color:#fff}
  .services h2{font-weight:400;font-size:28px;line-height:36px}
  .services p{font-size:18px;line-height:25px}
  .schedule{margin-top:40px;font-size:30px;line-height:41px}
  .schedule strong{font-weight:700;display:block}
  .schedule .url{font-size:25px;line-height:36px;display:block}
</style>
</head>
<body>
<main class="sheet">
  <div class="photo photo--staff" role="img" aria-label="Photo of two smiling female clinicians, a nurse with a clipboard and a doctor with a stethoscope"></div>
  <div class="photo photo--driver" role="img" aria-label="Photo of a blue semi truck cab beside a smiling truck driver in a cap"></div>
  <div class="fold fold--one"></div>
  <div class="fold fold--two"></div>

  <svg class="waves" viewBox="0 0 1200 929" aria-hidden="true">
    <defs>
      <linearGradient id="band" x1="0" y1="0" x2="0" y2="1">
        <stop offset="0" stop-color="#0455a3"/>
        <stop offset="1" stop-color="#0a3f8f"/>
      </linearGradient>
    </defs>
    <path d="M0,0 H413 V0 C300,15 150,30 0,70 Z" fill="#0455a3" opacity=".9"/>
    <path d="M0,0 H420 C300,8 160,20 0,45 Z" fill="#3f7fd0" opacity=".7"/>
    <path d="M0,420 C150,440 300,490 470,480 C650,470 850,390 1200,405 V929 H0 Z" fill="url(#band)"/>
    <path d="M0,445 C200,470 330,520 520,500 C700,480 900,420 1200,440 V470 C950,455 760,505 560,525 C380,545 200,500 0,480 Z" fill="#3f7fd0" opacity=".55"/>
    <path d="M0,560 C250,520 420,600 700,560 C900,530 1050,470 1200,480 V520 C1020,520 880,600 660,620 C430,640 250,580 0,600 Z" fill="#ffffff" opacity=".12"/>
    <path d="M820,500 C950,450 1080,440 1200,450 V470 C1080,465 960,480 820,500 Z" fill="#ffffff" opacity=".35"/>
  </svg>

  <div class="brand brand--small">Birchwell<br>Family Medicine</div>
  <div class="brand brand--large">Birchwell<br>Family Medicine</div>

  <section class="panel-center">
    <p class="cta-top"><span class="cta-lead">Schedule appointment</span>online through our website<br>www.kellanmoorclinic.com</p>
    <h2 class="visit-title">VISIT US</h2>
    <p class="address">4180 East Larkspur Road<br>Aldermoor Village, CO 80190</p>
    <p class="contact"><span>Phone (555) 014-2280</span><br><span>Fax &nbsp;&nbsp;&nbsp;&nbsp;&nbsp;&nbsp;(555) 014-2291</span></p>
  </section>

  <div class="map" role="img" aria-label="Street map showing the clinic location on the south side of Larkspur Road east of the interstate"></div>
  <p class="directions">Our office is located on the south side of Larkspur Road approximately one-half mile east of the I-40/Larkspur Road intersection (exit 212 of I-40). Our office is in a retail space near the Meadowlark Natural Market store.</p>

  <section class="about">
    <h2>About Us</h2>
    <p>Birchwell Family Medicine is a physician owned and operated medical practice in the Southgate Tech Center area of metro Denver, Colorado.</p>
    <p>Our mission is to provide commercial drivers with fast and convenient BFH exams by one of our QWLPA certified providers as well and BFH drug screening.</p>
  </section>

  <section class="services">
    <h2>We perform</h2>
    <p>Bureau of Freight Haulage (BFH) physical exams and also perform BFH drug testing onsite a</p>
    <p class="schedule"><strong>Schedule appointment</strong>online through our website<span class="url">www.kellanmoorclinic.com</span></p>
  </section>
</main>
</body>
</html>
```